Wix Website design for my therapy business - Willowmere Group

I have started designing a Wix site and have a good idea of what I want.
I have set up the pages, created some design ideas, and inputted the copy. I need someone fabulous to finish off the design aspects. I like working closely with the designers, I was an interior designer in an old career.
I would like the site to be funky but professional. My Wix skills are limited, and I just can't achieve the look I am wanting without having to spend a lot of time learning. If it's easier to start over, that's ok providing you use the same colours, font, images etc. I have included a screenshot of the home page below. I have another site I need to start as soon as we have finished this one.
I am looking for someone who is a good listener and is has design flare. I am easy to get along with and will respond quickly.
I would like to set up SEO and have help in the future.
Let me know if you are the right person for the job.
Target Market(s)
Please needing help with their mental health and for therapy.
Industry/Entity Type
Mental health
Font styles to use
Other font styles liked:
- Futura light
Requirements
Must have
- be easy to navigate and be simple yet stylish
Nice to have
- I have set up the basics of the site - nice to haves are already on the site
Should not have
- old fashioned large chunks of text.

```html
<!DOCTYPE html>
<html lang="en">
<head>
<meta charset="utf-8">
<title>Willowmere Group</title>
<link href="https://fonts.googleapis.com/css2?family=Poppins:wght@300;400;500;600;700&display=swap" rel="stylesheet">
<style>
:root{
  --brown:#9c8468;
  --brown-dark:#8a7257;
  --footer:#a58c6f;
  --ink:#2e2e2e;
  --body:#444;
  --cream:#ece6df;
  --white:#fff;
}
*{margin:0;padding:0;box-sizing:border-box}
html,body{width:1200px;height:3533px;overflow:hidden}
body{font-family:'Poppins',sans-serif;color:var(--body);background:var(--white);position:relative}
.abs{position:absolute}
.center{left:0;width:1200px;text-align:center}

/* header */
.brand{top:48px;font-size:38px;font-weight:500;color:var(--brown)}
.nav{top:148px;display:flex;justify-content:center;gap:25px;font-size:15px;color:#333}
.nav a{color:inherit;text-decoration:none;padding-bottom:6px}
.nav a.active{border-bottom:2px solid var(--brown)}
.header-line{top:197px;left:0;width:1200px;height:1px;background:#e5e5e5}

/* hero */
.hero{top:197px;left:0;width:1200px;height:567px;background:linear-gradient(120deg,#6b5a48,#b49474 45%,#8d7660 70%,#5e5042)}
.hero-kicker{top:520px;font-size:20px;color:var(--white);font-weight:400}
.hero-title{top:556px;font-size:48px;line-height:62px;font-weight:600;color:var(--white)}
.hero-chev{top:712px;left:584px}

/* section headings */
.kicker{font-size:21px;color:var(--brown);display:flex;align-items:center;justify-content:center;gap:6px}
.kicker::before,.kicker::after{content:"";width:50px;height:1px;background:var(--brown)}
.title{font-size:41px;font-weight:600;color:var(--ink)}

/* services */
.services-kicker{top:876px}
.services-title{top:902px}
.services-intro{top:958px;font-size:15px;line-height:26px;color:#333}
.service{top:1065px;width:260px;text-align:center}
.service .ring{width:153px;height:153px;margin:0 auto;border-radius:50%;border:2px dotted var(--brown);padding:10px}
.service .photo{width:100%;height:100%;border-radius:50%;background:radial-gradient(circle at 55% 45%,#d7c5b4,#8f7866 60%,#3a3330)}
.service h3{margin-top:20px;font-size:18px;font-weight:600;color:var(--brown)}
.service p{margin-top:6px;font-size:14.5px;line-height:24px;color:#333}
.service .more{width:22px;height:22px;border-radius:50%;background:var(--brown);margin:10px auto 0;display:flex;align-items:center;justify-content:center}

/* about */
.about-blob{top:1500px;left:56px}
.about-photo{top:1603px;left:119px;width:448px;height:448px;border-radius:50%;background:radial-gradient(circle at 45% 60%,#d1a582,#a77a58 50%,#3e3028)}
.about-kicker{top:1630px;left:650px;width:400px}
.about-title{top:1656px;left:650px;width:400px;text-align:center}
.about-text{top:1772px;left:655px;width:432px;font-size:15.5px;line-height:26px;text-align:justify;color:#333}
.btn{top:1920px;left:653px;width:186px;height:64px;border-radius:32px;background:var(--brown);color:var(--white);font-size:15px;display:flex;align-items:center;justify-content:center;gap:20px}
.btn .dot{width:24px;height:24px;border-radius:50%;background:#222;display:flex;align-items:center;justify-content:center}

/* testimonials */
.testi{top:2127px;left:0;width:1200px;height:513px;background:linear-gradient(100deg,#4d4540,#7b6a5c 45%,#8a7a68 65%,#5b5048)}
.quote{top:2205px;left:104px;font-size:170px;line-height:170px;font-weight:700;color:var(--white);font-family:Georgia,serif}
.testi-kicker{top:2234px}
.testi-kicker span{color:var(--brown)}
.testi-title{top:2260px;color:var(--white)}
.testi-text{top:2360px;font-size:15.5px;line-height:20px;color:var(--white)}
.arrow{width:44px;height:44px;border-radius:50%;background:rgba(40,40,40,.55);display:flex;align-items:center;justify-content:center}
.avatar{top:2457px;left:491px;width:88px;height:88px;border-radius:50%;background:linear-gradient(#c9ccd2,#2e3440);border:3px solid #eee}
.client{top:2470px;left:598px;color:var(--white)}
.client b{font-size:13px;font-weight:600;display:block}
.client small{font-size:9px;display:block;margin-top:2px}
.stars{margin-top:3px;display:flex;gap:2px}

/* resources */
.res-kicker{top:2732px}
.res-title{top:2760px}
.tile{top:2879px;height:252px;border-radius:24px}

/* footer */
.footer{top:3241px;left:0;width:1200px;height:292px;background:var(--footer);color:var(--white)}
.foot-brand{top:3290px;font-size:34px;font-weight:500;color:var(--white)}
.contact{top:3370px;display:flex;align-items:center;gap:12px;font-size:15px;line-height:19px;color:var(--white)}
.contact .ic{width:32px;height:32px;border-radius:50%;background:var(--white);display:flex;align-items:center;justify-content:center}
.vdiv{top:3370px;width:1px;height:38px;background:rgba(255,255,255,.7)}
.copy{top:3484px;left:89px;font-size:15px;color:var(--white)}
.social{top:3476px;width:36px;height:36px;border-radius:50%;border:1.5px solid var(--white)}
</style>
</head>
<body>

<header>
  <div class="abs center brand">Willowmere Group</div>
  <nav class="abs center nav">
    <a class="active">Home</a><a>About Me</a><a>EMDR</a><a>Addictions</a><a>Betrayal Trauma</a><a>PTSD</a><a>Program List</a><a>Resources</a><a>Blog</a><a>Contact Us</a>
  </nav>
  <div class="abs header-line"></div>
</header>

<section>
  <div class="abs hero" role="img" aria-label="Photo of a woman relaxing during a facial massage"></div>
  <div class="abs center hero-kicker">THE WILLOWMERE GROUP</div>
  <h1 class="abs center hero-title">Welcome To &nbsp;Our<br>Massage Therapy</h1>
  <svg class="abs hero-chev" width="32" height="20" viewBox="0 0 32 20"><path d="M2 3 L16 17 L30 3" fill="none" stroke="#fff" stroke-width="3"/></svg>
</section>

<section>
  <div class="abs center kicker services-kicker">OUR SERVICES</div>
  <h2 class="abs center title services-title">What We Do</h2>
  <p class="abs center services-intro">Lorem ipsum dolor sit amet, consectetur adipiscing elit, sed do eiusmodtempor<br>incididunt ut labore et dolore magnaaliquaUt enim ad minim</p>

  <div class="abs service" style="left:67px">
    <div class="ring"><div class="photo" role="img" aria-label="Photo of a client receiving a facial treatment"></div></div>
    <h3>EMDR</h3><p>Sample text. Lorem ipsum dolor<br>sit amet, consectetur adipi</p>
    <div class="more"><svg width="10" height="6"><path d="M1 1 L5 5 L9 1" fill="none" stroke="#fff" stroke-width="1.5"/></svg></div>
  </div>
  <div class="abs service" style="left:332px">
    <div class="ring"><div class="photo" role="img" aria-label="Photo of a client receiving a facial treatment"></div></div>
    <h3>ADDICTIONS</h3><p>Sample text. Lorem ipsum dolor<br>sit amet, consectetur adipi</p>
    <div class="more"><svg width="10" height="6"><path d="M1 1 L5 5 L9 1" fill="none" stroke="#fff" stroke-width="1.5"/></svg></div>
  </div>
  <div class="abs service" style="left:597px">
    <div class="ring"><div class="photo" role="img" aria-label="Photo of a client receiving a facial treatment"></div></div>
    <h3>BETRAYAL TRAUMA</h3><p>Sample text. Lorem ipsum dolor<br>sit amet, consectetur adipi</p>
    <div class="more"><svg width="10" height="6"><path d="M1 1 L5 5 L9 1" fill="none" stroke="#fff" stroke-width="1.5"/></svg></div>
  </div>
  <div class="abs service" style="left:869px">
    <div class="ring"><div class="photo" role="img" aria-label="Photo of a client receiving a facial treatment"></div></div>
    <h3>PTSD</h3><p>Sample text. Lorem ipsum dolor<br>sit amet, consectetur adipi</p>
    <div class="more"><svg width="10" height="6"><path d="M1 1 L5 5 L9 1" fill="none" stroke="#fff" stroke-width="1.5"/></svg></div>
  </div>
</section>

<section>
  <svg class="abs about-blob" width="530" height="520" viewBox="0 0 530 520">
    <path d="M265 0 C330 0 360 80 410 110 C480 150 540 150 525 240 C505 340 560 520 400 510 C300 505 200 540 120 470 C40 400 10 300 0 200 C-10 130 100 120 170 100 C215 85 205 0 265 0 Z" fill="var(--cream)"/>
  </svg>
  <div class="abs about-photo" role="img" aria-label="Photo of a therapist giving a back massage"></div>
  <div class="abs kicker about-kicker">ABOUT US</div>
  <h2 class="abs title about-title">Who We Are</h2>
  <p class="abs about-text">Lorem ipsum dolor sit amet, consefghctetur adipiscing elit, sed do eiusmod tempor incididunt ut labore et dolore magna aliqua. Ut enim ad minim veniam, quis nostrud exercitation ullamco laboris nisi ut</p>
  <div class="abs btn">KNOW MORE <span class="dot"><svg width="7" height="10"><path d="M1 1 L5 5 L1 9" fill="none" stroke="#fff" stroke-width="1.5"/></svg></span></div>
</section>

<section>
  <div class="abs testi" role="img" aria-label="Photo of massage hands on a client's back"></div>
  <div class="abs quote">&ldquo;</div>
  <div class="abs center kicker testi-kicker"><span>TESTIMONIALS</span></div>
  <h2 class="abs center title testi-title">What Our Clients Say</h2>
  <p class="abs center testi-text">Lorem ipsum, or lipsum as it is sometimes known, is dummy text used in laying out<br>print, graphic or web designs. The passage is attributed<br>unknown typesetter in the 15th century</p>
  <div class="abs arrow" style="top:2397px;left:72px"><svg width="10" height="16"><path d="M8 2 L2 8 L8 14" fill="none" stroke="#fff" stroke-width="2"/></svg></div>
  <div class="abs arrow" style="top:2397px;left:1091px"><svg width="10" height="16"><path d="M2 2 L8 8 L2 14" fill="none" stroke="#fff" stroke-width="2"/></svg></div>
  <div class="abs avatar" role="img" aria-label="Client portrait"></div>
  <div class="abs client">
    <b>Dana Whitlock</b><small>CEO, Northfield Co.</small>
    <div class="stars">
      <svg width="68" height="12" viewBox="0 0 68 12"><g fill="#f3d21c"><polygon points="6,0 7.5,4 12,4 8.5,7 10,12 6,9 2,12 3.5,7 0,4 4.5,4"/><polygon transform="translate(14 0)" points="6,0 7.5,4 12,4 8.5,7 10,12 6,9 2,12 3.5,7 0,4 4.5,4"/><polygon transform="translate(28 0)" points="6,0 7.5,4 12,4 8.5,7 10,12 6,9 2,12 3.5,7 0,4 4.5,4"/><polygon transform="translate(42 0)" points="6,0 7.5,4 12,4 8.5,7 10,12 6,9 2,12 3.5,7 0,4 4.5,4"/><polygon transform="translate(56 0)" points="6,0 7.5,4 12,4 8.5,7 10,12 6,9 2,12 3.5,7 0,4 4.5,4"/></g></svg>
    </div>
  </div>
</section>

<section>
  <div class="abs center kicker res-kicker">RESOURCES</div>
  <h2 class="abs center title res-title">Primary Care Is Our First Step</h2>
  <div class="abs tile" style="left:0;width:324px;border-radius:0 24px 24px 0;background:linear-gradient(135deg,#efe9e4,#d9c2ad)" role="img" aria-label="Photo of a neck and shoulder massage"></div>
  <div class="abs tile" style="left:332px;width:358px;background:linear-gradient(135deg,#e3e0de,#e8c9b5)" role="img" aria-label="Photo of a hand massage"></div>
  <div class="abs tile" style="left:701px;width:358px;background:linear-gradient(135deg,#f1eeec,#d7b8a2)" role="img" aria-label="Photo of a foot massage"></div>
  <div class="abs tile" style="left:1068px;width:132px;border-radius:24px 0 0 24px;background:linear-gradient(135deg,#b07a55,#6b4630)" role="img" aria-label="Photo of a shoulder massage"></div>
  <div class="abs" style="top:2994px;left:1066px;width:22px;height:22px;border-radius:50%;background:#222;display:flex;align-items:center;justify-content:center"><svg width="6" height="10"><path d="M1 1 L5 5 L1 9" fill="none" stroke="#fff" stroke-width="1.5"/></svg></div>
</section>

<footer>
  <div class="abs footer"></div>
  <div class="abs center foot-brand">Willowmere Group</div>
  <div class="abs contact" style="left:224px">
    <span class="ic"><svg width="16" height="16" viewBox="0 0 24 24"><path d="M6.6 10.8a15.1 15.1 0 006.6 6.6l2.2-2.2c.3-.3.7-.4 1-.2 1.1.4 2.3.6 3.6.6.6 0 1 .4 1 1V20c0 .6-.4 1-1 1A17 17 0 013 4c0-.6.4-1 1-1h3.5c.6 0 1 .4 1 1 0 1.3.2 2.5.6 3.6.1.3 0 .7-.2 1z" fill="var(--footer)"/></svg></span>
    <span>+1 555 010 2040<br>+1 555 010 2041</span>
  </div>
  <div class="abs vdiv" style="left:458px"></div>
  <div class="abs contact" style="left:516px">
    <span class="ic"><svg width="14" height="18" viewBox="0 0 14 18"><path d="M7 0a7 7 0 00-7 7c0 5 7 11 7 11s7-6 7-11a7 7 0 00-7-7zm0 9.5A2.5 2.5 0 117 4.5a2.5 2.5 0 010 5z" fill="var(--footer)"/></svg></span>
    <span>Dummy address here<br>Pin: 123456</span>
  </div>
  <div class="abs vdiv" style="left:775px"></div>
  <div class="abs contact" style="left:825px;top:3373px">
    <span class="ic"><svg width="16" height="12" viewBox="0 0 16 12"><rect x="0.5" y="0.5" width="15" height="11" fill="none" stroke="var(--footer)"/><path d="M1 1 L8 7 L15 1" fill="none" stroke="var(--footer)"/></svg></span>
    <span>hello@willowmere.example</span>
  </div>
  <div class="abs copy">Copyright @ 2023 All rights reserved</div>
  <div class="abs social" style="left:945px"></div>
  <div class="abs social" style="left:989px"></div>
  <div class="abs social" style="left:1032px"></div>
  <div class="abs social" style="left:1076px"></div>
</footer>

</body>
</html>
```